Private Chef booking platform landing page design

I need an amazing design for a landing page for my upcoming private chef booking platform Platerva. You can view my current page here: www.platerva.co.uk/mainindex.php. The design on this page is wrong right now. This platform is in Beta and the main purpose is to sign up chefs. Similar to what Rydexa.com is doing with their website -> become a driver. In my case we should have a button that says "become a chef", state the benefits of becoming a chef such as earning extra money, managing your time and bookings, increasing your client base and be creative with your food menus at the same time. Also, somewhere on the website it needs to say that we are currently in Beta mode and sign up to help us grow. In terms of visuals, I want the design to be sleek and clean and also adaptable to mobile devices as I am using html5. You can also re-design the current logo and choose any colours you think would be suitable for such a concept. Similar concept websites: hobwanderly.com and stovlin.com
Updates

Target Market(s)

upper middle class

Industry/Entity Type

Chef

Number of Pages Required

1 page

Font styles to use
Sans Serif

Requirements
Must have
• see brief and check hobwanderly.com and stovlin.com for inspiration and also rydexa.com
Nice to have
• see brief
Should not have
• bad visuals

```html
<!DOCTYPE html>
<html lang="en">
<head>
<meta charset="utf-8">
<title>Platerva — Chefs Made Meals In Your Home</title>
<link rel="stylesheet" href="https://fonts.googleapis.com/css2?family=Questrial&family=Lato:wght@400;700&family=Permanent+Marker&family=Rubik+Dirt&family=Great+Vibes&display=swap">
<style>
  :root {
    --orange: #e05400;
    --green: #78a00c;
    --green-button: #4f9c10;
    --teal: #10acbb;
    --red: #ac1c1e;
    --charcoal: #3a3a3a;
    --footer: #333132;
    --card-grey: #e8e8e8;
    --ink: #1c1c1c;
    --body-text: #555555;
    --white: #ffffff;
  }
  * { box-sizing: border-box; margin: 0; padding: 0; }
  html, body { width: 912px; height: 1200px; overflow: hidden; }
  body {
    position: relative;
    background: var(--white);
    font-family: "Questrial", "Century Gothic", sans-serif;
    color: var(--ink);
  }

  /* Header */
  .site-header { position: absolute; top: 0; left: 0; width: 912px; height: 55px; }
  .brand {
    position: absolute; left: 56px; top: 14px;
    display: flex; align-items: center; gap: 7px;
    font-size: 22px; color: var(--orange);
  }
  .brand-dot { width: 10px; height: 10px; border-radius: 50%; background: var(--orange); }
  .header-btn {
    position: absolute; top: 15px; width: 77px; height: 26px; border-radius: 3px;
    font-size: 12px; color: var(--white); text-transform: uppercase;
    display: flex; align-items: center; justify-content: center;
  }
  .header-btn--signup { left: 696px; background: var(--charcoal); }
  .header-btn--login { left: 779px; background: var(--orange); }

  /* Hero */
  .hero { position: absolute; top: 55px; left: 0; width: 912px; height: 477px; }
  .hero-photo {
    position: absolute; inset: 0;
    background:
      radial-gradient(ellipse at 50% 55%, rgba(240,238,232,0.9) 0%, rgba(200,196,188,0.6) 45%, rgba(90,82,72,0.7) 100%),
      linear-gradient(180deg, #8a7f72 0%, #d7d3cc 40%, #efefec 70%, #a59a8d 100%);
  }
  .hero-title { position: absolute; top: 170px; left: 0; width: 912px; text-align: center; color: var(--white); }
  .hero-title__line1 {
    display: block; font-family: "Permanent Marker", cursive;
    font-size: 48px; line-height: 50px; letter-spacing: 2px;
    text-shadow: 0 1px 3px rgba(0,0,0,0.35);
  }
  .hero-title__line2 {
    display: block; font-family: "Rubik Dirt", sans-serif;
    font-size: 44px; line-height: 44px; letter-spacing: 1px;
    text-shadow: 0 1px 3px rgba(0,0,0,0.35);
  }
  .pill {
    position: absolute; border-radius: 22px; color: var(--white);
    display: flex; align-items: center; justify-content: center;
    text-transform: uppercase;
    box-shadow: 0 2px 3px rgba(0,0,0,0.35);
  }
  .pill--chef { left: 183px; top: 322px; width: 262px; height: 41px; background: var(--orange); font-size: 19px; }
  .pill--how { left: 466px; top: 322px; width: 261px; height: 41px; background: var(--charcoal); font-size: 19px; }
  .pill--account {
    left: 366px; top: 518px; width: 180px; height: 27px; background: var(--green-button);
    font-size: 14px; box-shadow: none; border-radius: 14px;
  }

  /* Benefits */
  .benefits-title {
    position: absolute; top: 602px; left: 0; width: 912px; text-align: center;
    font-size: 21px; letter-spacing: 0.5px; font-weight: 700;
  }
  .benefit-card {
    position: absolute; top: 657px; width: 184px; height: 185px;
    border-radius: 4px; overflow: hidden; background: var(--card-grey);
  }
  .benefit-card svg.wave { position: absolute; top: 0; left: 0; }
  .benefit-card__icon { position: absolute; left: 62px; top: 20px; }
  .benefit-card__text {
    position: absolute; left: 14px; top: 128px; font-size: 15px; line-height: 16px; color: #2a2a2a;
  }
  .benefit-card--money { left: 56px; }
  .benefit-card--schedule { left: 261px; }
  .benefit-card--menus { left: 466px; }
  .benefit-card--clients { left: 672px; height: 182px; }

  /* Welcome */
  .welcome { position: absolute; top: 905px; left: 0; width: 912px; text-align: center; }
  .welcome__lead { display: block; font-family: "Great Vibes", cursive; font-size: 22px; color: var(--ink); padding-left: 40px; }
  .welcome__brand { display: block; font-size: 40px; color: var(--orange); margin-top: 2px; }
  .welcome__copy {
    position: absolute; top: 1000px; left: 130px; width: 652px; text-align: center;
    font-family: "Lato", sans-serif; font-size: 11px; line-height: 19.5px; color: var(--body-text);
  }

  /* Footer */
  .site-footer {
    position: absolute; top: 1117px; left: 0; width: 912px; height: 83px;
    background: var(--footer); color: var(--white); font-family: "Lato", sans-serif;
  }
  .social-links { position: absolute; top: 24px; left: 0; width: 912px; display: flex; justify-content: center; gap: 14px; list-style: none; }
  .social-links li { display: flex; align-items: center; gap: 5px; font-size: 11px; text-transform: uppercase; }
  .social-links li::before { content: ""; width: 11px; height: 11px; background: var(--white); border-radius: 2px; }
  .copyright { position: absolute; top: 54px; left: 0; width: 912px; text-align: center; font-size: 10px; font-weight: 700; letter-spacing: 0.3px; }
</style>
</head>
<body>

<header class="site-header">
  <div class="brand"><span class="brand-dot"></span>Platerva</div>
  <a class="header-btn header-btn--signup">Sign up</a>
  <a class="header-btn header-btn--login">Login</a>
</header>

<section class="hero">
  <div class="hero-photo" role="img" aria-label="Photo of five smiling chefs in white uniforms and toques standing in a professional kitchen"></div>
  <h1 class="hero-title">
    <span class="hero-title__line1">CHEFS MADE MEALS</span>
    <span class="hero-title__line2">IN YOUR HOME</span>
  </h1>
  <a class="pill pill--chef">Become a private chef</a>
  <a class="pill pill--how">How it works on it</a>
</section>
<a class="pill pill--account">Create an account</a>

<h2 class="benefits-title">FOR YOUR BENEFITS</h2>

<div class="benefit-card benefit-card--money">
  <svg class="wave" width="184" height="185" viewBox="0 0 184 185"><path d="M0 0H184V96C160 92 140 76 110 76C80 76 60 90 0 92Z" fill="var(--orange)"/></svg>
  <svg class="benefit-card__icon" width="60" height="55" viewBox="0 0 60 55" fill="none" stroke="#fff" stroke-width="3">
    <rect x="6" y="12" width="22" height="6" fill="#fff"/><rect x="6" y="20" width="22" height="6" fill="#fff"/><rect x="6" y="28" width="22" height="6" fill="#fff"/><rect x="6" y="36" width="22" height="6" fill="#fff"/>
    <rect x="26" y="4" width="22" height="5" fill="#fff"/><rect x="26" y="11" width="22" height="5" fill="#fff"/>
    <circle cx="38" cy="35" r="14" fill="var(--orange)"/>
    <text x="38" y="42" text-anchor="middle" font-size="19" font-family="Lato, sans-serif" font-weight="700" fill="#fff" stroke="none">$</text>
  </svg>
  <p class="benefit-card__text">Earn<br>extra money</p>
</div>

<div class="benefit-card benefit-card--schedule">
  <svg class="wave" width="184" height="185" viewBox="0 0 184 185"><path d="M0 0H184V94C150 92 130 110 96 110C60 110 40 94 0 96Z" fill="var(--green)"/></svg>
  <svg class="benefit-card__icon" width="60" height="55" viewBox="0 0 60 55" fill="none" stroke="#fff" stroke-width="3">
    <rect x="7" y="9" width="34" height="32" rx="2"/><line x1="7" y1="18" x2="41" y2="18"/>
    <line x1="15" y1="4" x2="15" y2="12"/><line x1="33" y1="4" x2="33" y2="12"/>
    <g fill="#fff" stroke="none"><rect x="12" y="23" width="5" height="5"/><rect x="21" y="23" width="5" height="5"/><rect x="12" y="31" width="5" height="5"/><rect x="21" y="31" width="5" height="5"/></g>
    <circle cx="42" cy="39" r="10" fill="var(--green)"/><polyline points="42,33 42,39 46,41"/>
  </svg>
  <p class="benefit-card__text">Fully manage your<br>bookings schedule</p>
</div>

<div class="benefit-card benefit-card--menus">
  <svg class="wave" width="184" height="185" viewBox="0 0 184 185"><path d="M0 0H184V92C150 90 120 112 88 112C56 112 30 90 0 94Z" fill="var(--teal)"/></svg>
  <svg class="benefit-card__icon" width="60" height="55" viewBox="0 0 60 55">
    <path d="M6 10L28 14V46L6 42Z M54 10L32 14V46L54 42Z" fill="#fff"/>
    <g stroke="var(--teal)" stroke-width="2.5" stroke-linecap="round"><line x1="20" y1="38" x2="40" y2="20"/><line x1="20" y1="20" x2="40" y2="38"/></g>
  </svg>
  <p class="benefit-card__text">Be creative with your<br>food menus</p>
</div>

<div class="benefit-card benefit-card--clients">
  <svg class="wave" width="184" height="182" viewBox="0 0 184 182"><path d="M0 0H184V92C160 92 140 108 108 108C76 108 40 94 0 94Z" fill="var(--red)"/></svg>
  <svg class="benefit-card__icon" width="60" height="55" viewBox="0 0 60 55" fill="none" stroke="#fff" stroke-width="2.5">
    <line x1="30" y1="16" x2="16" y2="36"/><line x1="30" y1="16" x2="44" y2="36"/><line x1="16" y1="36" x2="44" y2="36"/>
    <g fill="var(--red)"><circle cx="30" cy="13" r="9"/><circle cx="15" cy="37" r="9"/><circle cx="45" cy="37" r="9"/></g>
    <g fill="#fff" stroke="none"><circle cx="30" cy="11" r="3"/><path d="M25 18a5 4 0 0 1 10 0Z"/><circle cx="15" cy="35" r="3"/><path d="M10 42a5 4 0 0 1 10 0Z"/><circle cx="45" cy="35" r="3"/><path d="M40 42a5 4 0 0 1 10 0Z"/></g>
  </svg>
  <p class="benefit-card__text">Expand your<br>client base</p>
</div>

<section class="welcome">
  <span class="welcome__lead">Welcome to</span>
  <span class="welcome__brand">Platerva</span>
</section>
<p class="welcome__copy">Lorem Ipsum is simply dummy text of the printing and typesetting industry. Lorem Ipsum has been the industry's standard dummy text ever since the 1500s, when an unknown printer took a galley of type and scrambled it to make a type specimen book. It has survived not only five centuries, but also the leap into electronic typesetting, remaining essentially unchanged.</p>

<footer class="site-footer">
  <ul class="social-links">
    <li>Chirpwell</li>
    <li>Facetrail</li>
    <li>Viewtube</li>
    <li>Searchly+</li>
    <li>Linkfolio</li>
  </ul>
  <p class="copyright">© 2015 PLATERVA. ALL RIGHTS RESERVED.</p>
</footer>

</body>
</html>
```